House Church design model for faith-based organization

A design is needed for a house church model (Christian, faith-based). I’m looking for a graphic to convey four house church hallmarks showing the balance of member engagement. The four-part model includes - God’s Presence, Community, Discipleship, Outreach. The model should consist of the text for the four parts and the words - House Church

Perhaps a circular/modular design with House Church in the center. Using equally-sized interlocking slices or winged parts (graphically speaking, but not angelic wings) may help convey a balanced approach. It isn’t a process and should not appear in progressive steps, but the order (as listed) is used when explaining the concept. The model will be used for members to evaluate monthly focus.

I’m open to interpretation of the design and artwork. Designers should not feel a need to utilize cliché-like Christian symbols. However, if done minimally (and perhaps first century-like), they could be of interest (but are not required). Keeping it abstract may help readability and convey a roots/back-to-basics feel.

The artwork will be used for a video and PowerPoint presentation. It should be vector-based for simple movement/animation.

Additional thoughts:
Readable, not complex
Interesting interlocking design found at: https://www.plorvexia.com/circle-element-infographic-options-parts-steps-template-cycle-diagram-graph-round-chart-image572914386

Target Market(s)

To existing members (for reflection) and for those seeking a simpler church experience.

Requirements
Must have
• Simple, readable design, ability to reproduce for PowerPoint, video, and web. Prefer simple illustrations rather than images.
Nice to have
• The design should create a calming sense of focus on four priorities vs. the complexity of structure/requirements often found in the church experience.
Should not have
• Not crazy about puzzle pieces. Please avoid using all CAPS and serif fonts. Should not use complex images or photos.

```html
<!DOCTYPE html>
<html lang="en">
<head>
<meta charset="utf-8">
<title>Home Church – Four Hallmarks</title>
<link rel="stylesheet" href="https://fonts.googleapis.com/css2?family=Exo+2:wght@700&family=Kanit:wght@600&display=swap">
<style>
  :root {
    --presence: #fe2837;
    --community: #fdc500;
    --discipleship: #0ab2ca;
    --outreach: #075381;
    --ink: #050505;
    --paper: #fefefe;
    --label: #ffffff;
  }
  html, body {
    margin: 0;
    padding: 0;
    width: 1200px;
    height: 1200px;
    overflow: hidden;
    background: var(--paper);
  }
  .hallmark-model {
    display: block;
    width: 1200px;
    height: 1200px;
  }
  .segment--presence { fill: var(--presence); }
  .segment--community { fill: var(--community); }
  .segment--discipleship { fill: var(--discipleship); }
  .segment--outreach { fill: var(--outreach); }
  .segment-label {
    font-family: "Exo 2", sans-serif;
    font-weight: 700;
    font-size: 88px;
    fill: var(--label);
    letter-spacing: 2px;
  }
  .hallmark-icon {
    fill: var(--label);
    opacity: 0.28;
  }
  .center-title {
    font-family: "Kanit", sans-serif;
    font-weight: 600;
    fill: var(--ink);
  }
</style>
</head>
<body>
<svg class="hallmark-model" viewBox="0 0 1920 1920" xmlns="http://www.w3.org/2000/svg" aria-labelledby="model-title">
  <title id="model-title">Home Church: God's Presence, Community, Discipleship, Outreach</title>
  <defs>
    <path id="wing-shape" d="M512,466
      C760,240 1150,230 1405,450
      C1470,640 1475,880 1340,1010
      C1290,1065 1235,1112 1172,1148
      C1222,1062 1242,962 1226,870
      C1202,702 1122,600 990,545
      C840,470 680,440 515,472 Z"/>
    <path id="arc-top" d="M365,965 A600,600 0 0 1 1565,965"/>
    <path id="arc-right" d="M965,1605 A640,640 0 0 0 965,325"/>
    <path id="arc-bottom" d="M335,965 A630,630 0 0 0 1595,965"/>
    <path id="arc-left" d="M965,1560 A595,595 0 0 1 965,370"/>
  </defs>

  <g class="segments">
    <use href="#wing-shape" class="segment--community"/>
    <use href="#wing-shape" class="segment--discipleship" transform="rotate(90 965 965)"/>
    <use href="#wing-shape" class="segment--outreach" transform="rotate(180 965 965)"/>
    <use href="#wing-shape" class="segment--presence" transform="rotate(270 965 965)"/>
  </g>

  <g class="segment-labels">
    <text class="segment-label"><textPath href="#arc-top" startOffset="51.5%" text-anchor="middle">Community</textPath></text>
    <text class="segment-label"><textPath href="#arc-right" startOffset="46%" text-anchor="middle">Discipleship</textPath></text>
    <text class="segment-label"><textPath href="#arc-bottom" startOffset="54%" text-anchor="middle">Outreach</textPath></text>
    <text class="segment-label"><textPath href="#arc-left" startOffset="60%" text-anchor="middle">God’s Presence</textPath></text>
  </g>

  <g class="hallmark-icons">
    <circle class="hallmark-icon" cx="648" cy="640" r="110" role="img" aria-label="Dove icon representing God's presence"/>
    <circle class="hallmark-icon" cx="1248" cy="545" r="110" role="img" aria-label="Group of people around a doorway representing community"/>
    <circle class="hallmark-icon" cx="1320" cy="1270" r="110" role="img" aria-label="Three figures with a cross, globe and dove representing discipleship"/>
    <circle class="hallmark-icon" cx="675" cy="1360" r="110" role="img" aria-label="Globe with connected network nodes representing outreach"/>
  </g>

  <g class="center-title">
    <text x="958" y="992" text-anchor="middle" font-size="112">Home</text>
    <text x="958" y="1102" text-anchor="middle" font-size="122">Church</text>
  </g>
</svg>
</body>
</html>
```